Business Card Design Project

I have a two letter domain name qo.com.au (lower case font please). I want a business card, cum logo that is die cut (around the qo segment at least) that fits standard business card size.
qo is all about what 'I am' - a journalist, blogger, analyst, commentator. My mantra is "I wander so qo'.
The reverse of the card only needs my name Lon Fitch, email lon@qo.com.au and mobile +61 400 555 817
Target Market(s)
Mainly people that will use my professional writing services and suppliers that will provide product for review
Industry/Entity Type
Business
Requirements
Must have
- One side is qo.com.au (hint - the .com.au can be vertical or horizontal to fit - the qo should be as large as possible).
The other requires large size font name, email and phone details (so no one needs glasses to read it).
The die cut can be just to highlight the qo segment - need not be around the whole card.
Font used in the past was Belwe (old style - very much like the i used in the information symbol).
Colours - no preference - prefer two colour to process colour but can also be an outline font instead of solid colour.

```html
<!DOCTYPE html>
<html lang="en">
<head>
<meta charset="utf-8">
<title>qo.com.au — Business Card</title>
<link rel="stylesheet" href="https://fonts.googleapis.com/css2?family=Cinzel:wght@500&family=Poiret+One&display=swap">
<style>
  :root {
    --page: #ffffff;
    --card-edge: #1a1a1a;
    --card-glow: #3b3b3b;
    --card-dark: #1f1f1f;
    --frame: #9a9a9a;
    --ink-light: #ffffff;
    --ink-soft: #e6e6e6;
    --accent: #e2562a;
  }
  * { margin: 0; padding: 0; box-sizing: border-box; }
  html, body {
    width: 1200px; height: 900px; overflow: hidden;
    background: var(--page);
  }
  .sheet { position: relative; width: 1200px; height: 900px; }

  .card {
    position: absolute; left: 262px; width: 739px; height: 393px;
    border: 1px solid var(--card-edge);
    background: radial-gradient(ellipse 60% 70% at 50% 50%, var(--card-glow) 0%, #2c2c2c 45%, var(--card-dark) 100%);
  }
  .card--front { top: 58px; }
  .card--back { top: 476px; }
  .card__frame { position: absolute; border: 2px solid var(--frame); opacity: .85; }
  .card--front .card__frame { left: 8px; top: 11px; right: 12px; bottom: 13px; }
  .card--back .card__frame { left: 9px; top: 13px; right: 12px; bottom: 11px; border-width: 1px; }

  .brand-name {
    position: absolute; left: 0; right: 0; top: 150px;
    text-align: center; white-space: nowrap;
    font-family: "Poiret One", sans-serif; font-weight: 400;
    font-size: 96px; line-height: 110px;
    color: var(--ink-light);
  }

  .tagline {
    position: absolute; left: 0; right: 0; text-align: center;
    font-family: "Poiret One", sans-serif; text-transform: uppercase;
    letter-spacing: .02em; white-space: nowrap;
  }
  .tagline--roles { top: 331px; font-size: 13px; color: var(--accent); }
  .tagline--mantra { top: 351px; font-size: 13px; color: var(--ink-soft); }

  .owner-name {
    position: absolute; left: 110px; top: 172px; width: 240px; text-align: right;
    font-family: "Poiret One", sans-serif; font-weight: 400; font-size: 36px; line-height: 44px;
    text-transform: uppercase; color: var(--accent); letter-spacing: .02em; white-space: nowrap;
  }
  .divider {
    position: absolute; left: 372px; top: 146px; width: 2px; height: 99px;
    background: var(--ink-light);
  }
  .contact {
    position: absolute; left: 420px; top: 166px; color: var(--ink-soft);
    font-style: normal; white-space: nowrap;
  }
  .contact__email {
    display: block; font-family: "Cinzel", serif; font-weight: 500; font-size: 22px;
    text-transform: uppercase; letter-spacing: .03em; line-height: 30px;
  }
  .contact__phone {
    display: block; font-family: "Poiret One", sans-serif; font-size: 22px;
    line-height: 30px; letter-spacing: .02em;
  }
</style>
</head>
<body>
<main class="sheet">
  <section class="card card--front" aria-label="Card front">
    <div class="card__frame"></div>
    <p class="brand-name">qo.com.au</p>
    <p class="tagline tagline--roles">A Journalist | A Blogger | An Analyst | A Commentator</p>
    <p class="tagline tagline--mantra">I wander so qo'</p>
  </section>

  <section class="card card--back" aria-label="Card back">
    <div class="card__frame"></div>
    <h1 class="owner-name">Lon Fitch</h1>
    <div class="divider"></div>
    <address class="contact">
      <span class="contact__email">lon@qo.com.au</span>
      <span class="contact__phone">+61 400 555 817</span>
    </address>
  </section>
</main>
</body>
</html>
```